5x8" package design for beauty / skin care product in a mylar bag

Brisomel Labs’ Glycolic Acid Powder is pure glycolic acid powder that, when mixed with water, creates glycolic acid solution. Depending on the amount of water added to the powder, you can create different strengths of the solution. Commerical products use between 10 and 70% glycolic acid solution in products. Brisomel Labs is part of the Brisomel hair care company. One of our products use glycolic acid and we can repurpose the raw ingredient alone for retail sales targeting do-it-yourself at home beauty and skin care makers.

Most sellers of glycolic acid powder use basic packaging. Brisomel Labs intends to create professional, standout packaging that reinforces the quality of the glycolic acid powder we are selling and is consistent with other Brisomel brand products sold.

Package design is for a 5x8" matte finished, top loading, resealable pouch. Just looking for front design initially. Second project will include back pouch design using format or design from the front of package.

```html
<!DOCTYPE html>
<html lang="en">
<head>
<meta charset="utf-8">
<title>Brisomel Labs — Glycolic Acid Powder pouch front</title>
<link rel="stylesheet" href="https://fonts.googleapis.com/css2?family=Inter:wght@500;700;800&display=swap">
<style>
  :root {
    --bg: #ebebeb;
    --pouch: #0e4a42;
    --pouch-deep: #093c35;
    --band-mid: #5f98a0;
    --band-edge: #1f5c5a;
    --text-light: #f1f1ef;
    --text-mint: #cfe6df;
    --badge: #a54eb0;
    --badge-light: #b768c0;
    --powder: #f4f4f4;
    --powder-shade: #dedede;
  }
  * { margin: 0; padding: 0; box-sizing: border-box; }
  html, body { width: 1200px; height: 1200px; overflow: hidden; background: var(--bg); }
  body { position: relative; font-family: "Inter", Arial, sans-serif; }

  .pouch {
    position: absolute; left: 276px; top: 88px;
    width: 648px; height: 1024px;
    background: linear-gradient(180deg, var(--pouch) 0%, var(--pouch-deep) 60%, var(--pouch) 100%);
    border-radius: 26px 26px 18px 18px;
    overflow: hidden;
  }
  .tear-notch {
    position: absolute; top: 64px; width: 8px; height: 8px; border-radius: 50%;
    background: var(--bg);
  }
  .tear-notch.left { left: -4px; }
  .tear-notch.right { right: -4px; }
  .zipper {
    position: absolute; left: 30px; right: 30px; top: 128px; height: 8px;
    border-top: 1px solid rgba(255,255,255,0.12);
    border-bottom: 1px solid rgba(255,255,255,0.12);
  }

  .reseal-tag {
    position: absolute; left: 455px; top: 178px; width: 134px;
    padding: 4px 0 3px;
    border-top: 1.5px solid var(--text-mint);
    border-bottom: 1.5px solid var(--text-mint);
    color: var(--text-mint); font-size: 12.5px; font-weight: 700; letter-spacing: 0.5px;
    text-align: center; transform: rotate(-2deg);
  }

  .brand-name {
    position: absolute; left: 0; right: 0; top: 282px;
    text-align: center; color: var(--text-light);
    font-size: 70px; font-weight: 500; line-height: 78px; letter-spacing: 1px;
  }

  .title-band {
    position: absolute; left: 0; right: 0; top: 462px; height: 160px;
    background: linear-gradient(90deg, var(--band-edge) 0%, var(--band-mid) 45%, var(--band-mid) 55%, var(--band-edge) 100%);
    border-bottom: 2px solid rgba(207,230,223,0.6);
    transform: skewY(-0.6deg);
  }
  .product-title {
    position: absolute; left: 0; right: 0; top: 490px;
    text-align: center; color: var(--text-light);
    font-size: 62px; font-weight: 800; line-height: 64px; letter-spacing: -0.5px;
  }
  .use-list {
    position: absolute; left: 0; right: 0; top: 630px;
    text-align: center; color: var(--text-mint);
    font-size: 14px; font-weight: 700; letter-spacing: 0.2px; word-spacing: 2px;
  }

  .powder-photo { position: absolute; left: 0; top: 660px; width: 648px; height: 364px; }

  .free-from-badge {
    position: absolute; left: 410px; top: 712px; width: 260px; height: 118px;
    background: linear-gradient(90deg, var(--badge-light), var(--badge));
    border-radius: 40px 0 0 40px;
    transform: rotate(-8deg); transform-origin: left center;
    display: flex; align-items: center; padding-left: 26px; gap: 10px;
    color: var(--text-light);
  }
  .free-from-badge .zero { font-size: 50px; font-weight: 800; letter-spacing: -1px; }
  .free-from-badge ul { list-style: none; font-size: 12.5px; font-weight: 700; line-height: 19px; }
</style>
</head>
<body>
  <div class="pouch">
    <span class="tear-notch left"></span>
    <span class="tear-notch right"></span>
    <div class="zipper"></div>

    <div class="reseal-tag">RESEALABLE BAG</div>

    <div class="brand-name">Brisomel<br>Labs</div>

    <div class="title-band"></div>
    <h1 class="product-title">GLYCOLIC ACID<br>POWDER</h1>
    <p class="use-list">FACIAL &nbsp;•&nbsp; TONER &nbsp;•&nbsp; SCALP SCRUB &nbsp;•&nbsp; HYPERPIGMENTATION</p>

    <svg class="powder-photo" viewBox="0 0 648 364" role="img" aria-label="Photograph of a mound of white glycolic acid powder">
      <defs>
        <linearGradient id="powderFill" x1="0" y1="0" x2="0" y2="1">
          <stop offset="0" stop-color="var(--powder)"/>
          <stop offset="1" stop-color="var(--powder-shade)"/>
        </linearGradient>
      </defs>
      <polygon points="317,90 648,330 648,364 0,364 0,330" fill="url(#powderFill)"/>
    </svg>

    <div class="free-from-badge">
      <span class="zero">0%</span>
      <ul>
        <li>Fragrances</li>
        <li>Additives</li>
        <li>Dyes</li>
      </ul>
    </div>
  </div>
</body>
</html>
```